Staff Falcons WIX Design Project - website for HR Professional Community

Redesign of website to incorporate new logo - we are looking for a web design partner - will include adhoc work going forward.

Current website - www.thestafffalcons.co.uk

The 'Onward to Radiant' content is not required on the new site.

Target Market(s)

HR professionals

Industry/Entity Type

Professional Network

Coding

Coded - Design and coding required

Requirements
Must have
• A partners page
Nice to have
• an events page

```html
<!DOCTYPE html>
<html lang="en">
<head>
<meta charset="utf-8">
<title>Staff Falcons</title>
<link rel="stylesheet" href="https://fonts.googleapis.com/css2?family=Roboto:ital,wght@0,300;0,400;0,500;0,700;1,400&display=swap">
<style>
:root{
  --ink:#1b1c1e;
  --dark:#1e1f22;
  --orange:#f0861a;
  --text:#222;
  --muted:#555;
  --white:#fff;
  --card-shadow:0 2px 8px rgba(0,0,0,.12);
}
*{box-sizing:border-box;margin:0;padding:0}
html,body{width:1200px;height:3677px;overflow:hidden}
body{font-family:"Roboto",Arial,sans-serif;color:var(--text);background:var(--white);position:relative}

/* header */
.site-header{position:absolute;left:0;top:0;width:1200px;height:83px;background:var(--dark)}
.brand{position:absolute;left:111px;top:7px;width:126px;display:flex;flex-direction:column;align-items:center;gap:6px;color:var(--orange);font-size:16px;font-weight:500;letter-spacing:.5px;white-space:nowrap}
.brand-dot{width:28px;height:28px;border-radius:50%;background:var(--orange)}
.main-nav{position:absolute;left:295px;top:31px;display:flex;gap:30px;font-size:17px;font-weight:500;color:var(--white);white-space:nowrap}
.main-nav .active{color:var(--orange)}
.nav-social{position:absolute;left:1036px;top:31px;display:flex;align-items:center;gap:10px;color:var(--white)}
.nav-social .sep{font-size:17px}
.social-dot{width:11px;height:11px;border-radius:50%;background:var(--white)}

/* hero */
.hero{position:absolute;left:0;top:83px;width:1200px;height:643px;background:linear-gradient(100deg,#e9f3f6 0%,#d6e9ef 35%,#b9cfd8 60%,#c9d8dc 80%,#e4ecee 100%)}
.hero-title{position:absolute;left:111px;top:250px;font-size:51px;font-weight:700;color:var(--ink);white-space:nowrap}
.hero-lead{position:absolute;left:111px;top:322px;width:400px;font-size:17px;font-weight:500;line-height:26px;color:var(--ink)}
.btn{display:inline-flex;align-items:center;justify-content:center;background:var(--orange);color:var(--white);font-weight:500}
.hero-btn{position:absolute;left:111px;top:401px;width:169px;height:49px;font-size:16px}
.scroll-cue{position:absolute;left:590px;top:590px}

/* services */
.card{position:absolute;background:var(--white);box-shadow:var(--card-shadow);text-align:center}
.card-media{height:200px}
.card-title{margin-top:24px;font-size:26px;font-weight:500;color:var(--ink)}
.card-text{margin:16px auto 0;width:270px;font-size:14px;line-height:26px;color:var(--muted)}
.card-btn{position:absolute;left:16px;right:16px;bottom:15px;height:41px;font-size:15px}

/* job board */
.jobs{position:absolute;left:0;top:1338px;width:1200px;height:562px;background:var(--dark)}
.jobs-media{position:absolute;left:601px;top:0;width:599px;height:562px;background:linear-gradient(160deg,#d8dde0 0%,#a9b0b3 45%,#6c6a66 70%,#e8e6e3 100%)}
.jobs-title{position:absolute;left:112px;top:86px;font-size:37px;font-weight:700;line-height:40px;color:var(--white);white-space:nowrap}
.jobs-rule{position:absolute;left:112px;top:170px;width:146px;height:3px;background:var(--orange)}
.jobs-copy{position:absolute;left:112px;top:197px;width:450px;font-size:17px;line-height:33px;color:var(--white)}
.jobs-copy p+p{margin-top:9px}
.jobs-btn{position:absolute;left:112px;top:426px;width:146px;height:43px;font-size:16px}

/* testimonial */
.testimonial{position:absolute;left:0;top:1900px;width:1200px;height:429px;background:var(--orange);text-align:center;color:var(--white)}
.quote-mark{position:absolute;left:579px;top:92px}
.quote-text{position:absolute;left:180px;top:152px;width:840px;font-size:20px;font-style:italic;line-height:33px}
.quote-author{position:absolute;left:0;width:1200px;top:272px;font-size:19px;font-weight:500}
.dots{position:absolute;left:558px;top:323px;display:flex;gap:12px}
.dots span{width:12px;height:12px;border-radius:50%;background:rgba(255,255,255,.5)}
.dots .on{background:var(--white)}

/* team */
.team-title{position:absolute;left:0;width:1200px;top:2402px;text-align:center;font-size:38px;font-weight:500;color:var(--ink)}
.team-rule{position:absolute;left:528px;top:2460px;width:146px;height:3px;background:var(--orange)}
.member-media{height:200px;background:linear-gradient(180deg,#9a9a9a,#cfcfcf)}
.member-badge{position:absolute;left:125px;top:170px;width:60px;height:60px;border-radius:50%;background:var(--orange)}
.member-name{margin-top:48px;font-size:27px;font-weight:500;color:var(--ink);white-space:nowrap}
.member-role{margin-top:6px;font-size:16px;color:#444}
.member-bio{margin:14px auto 0;width:270px;font-size:14px;line-height:26px;color:var(--muted)}

/* footer */
.site-footer{position:absolute;left:0;top:2994px;width:1200px;height:683px;background:var(--dark);color:var(--white)}
.footer-rule{position:absolute;left:113px;top:94px;width:47px;height:2px;background:var(--white)}
.footer-heading{position:absolute;left:113px;top:118px;font-size:22px;font-weight:700}
.footer-line{position:absolute;left:113px;font-size:19px}
.footer-social{position:absolute;left:113px;top:386px;display:flex;gap:18px}
.footer-social span{width:20px;height:20px;border-radius:50%;background:var(--white)}
.copyright{position:absolute;left:114px;top:482px;font-size:14px}
.form-label{position:absolute;left:655px;font-size:14px}
.field{position:absolute;left:657px;width:433px;border:1px solid #bbb;border-radius:2px;background:transparent}
.submit-btn{position:absolute;left:925px;top:574px;width:163px;height:49px;font-size:16px}
</style>
</head>
<body>

<header class="site-header">
  <div class="brand"><span class="brand-dot"></span>STAFF FALCONS</div>
  <nav class="main-nav">
    <span class="active">HOME</span><span>NEWSLETTER</span><span>OUR STORY</span><span>PARTNERS</span><span>EVENTS</span><span>TEAM</span><span>CONTACT US</span>
  </nav>
  <div class="nav-social"><span class="sep">|</span><span class="social-dot" aria-label="Social link"></span><span class="social-dot" aria-label="Social link"></span></div>
</header>

<section class="hero" role="img" aria-label="Photo of a professional woman in a meeting at an office table">
  <h1 class="hero-title">THE STAFF FALCONS</h1>
  <p class="hero-lead">Lorem ipsum dolor sit amet, consecter adipiscing elit, sed do eiusmod tempor incididunt</p>
  <span class="btn hero-btn">GET STARTED</span>
  <svg class="scroll-cue" width="20" height="30" viewBox="0 0 20 30"><rect x="2" y="2" width="16" height="26" rx="8" fill="none" stroke="#111" stroke-width="2"/><line x1="10" y1="8" x2="10" y2="13" stroke="#111" stroke-width="2"/></svg>
</section>

<section class="services">
  <article class="card" style="left:111px;top:810px;width:310px;height:441px">
    <div class="card-media" role="img" aria-label="Photo of many hands stacked together" style="background:linear-gradient(135deg,#5b6670,#a27a5c,#3e4a57)"></div>
    <h2 class="card-title">COMMUNITY</h2>
    <p class="card-text">Our Circlehall Community Group enables you to connect with a fast-growing, highly engaged community of over 17k HR professionals</p>
    <span class="btn card-btn">Join our Circlehall Group</span>
  </article>
  <article class="card" style="left:445px;top:810px;width:310px;height:441px">
    <div class="card-media" role="img" aria-label="Photo of a handshake over a desk with a laptop" style="background:linear-gradient(135deg,#c9b79b,#8a7f72,#e6e2db)"></div>
    <h2 class="card-title">JOBS</h2>
    <p class="card-text">Get your HR job in front of 17k HR Professionals FREE job postings for members of our Circlehall group Open to non-members ONLY £100+vat</p>
    <span class="btn card-btn">Join our Circlehall Group</span>
  </article>
  <article class="card" style="left:779px;top:810px;width:310px;height:441px">
    <div class="card-media" role="img" aria-label="Photo of a coaching session in a bright office" style="background:linear-gradient(135deg,#e9ecee,#9aa0a5,#3b3f44)"></div>
    <h2 class="card-title">COACHING</h2>
    <p class="card-text">Our coaching club is currently over subscribed and we are not currently accepting requests for support .Doors are open now for registrations!</p>
    <span class="btn card-btn">Join our Circlehall Group</span>
  </article>
</section>

<section class="jobs">
  <h2 class="jobs-title">THE STAFF FALCONS JOB<br>BOARD!</h2>
  <div class="jobs-rule"></div>
  <div class="jobs-copy">
    <p>Are you looking to share your HR roles with our audience? Are you an HR job seeker looking for your next adventure?</p>
    <p>We are fast becoming THE place to share and seek for HR jobs in the UK</p>
    <p>(and get this!... If you're a member of our Circlehall group you can share your jobs for FREE!)</p>
  </div>
  <span class="btn jobs-btn">View Job</span>
  <div class="jobs-media" role="img" aria-label="Photo of colleagues smiling around a laptop in an office"></div>
</section>

<section class="testimonial">
  <svg class="quote-mark" width="42" height="34" viewBox="0 0 42 34"><path d="M2 32V19C2 9 7 3 16 1l2 5c-5 2-7 5-7 9h7v17zM24 32V19c0-10 5-16 14-18l2 5c-5 2-7 5-7 9h7v17z" fill="#fff"/></svg>
  <p class="quote-text">I came across the Staff Falcons community on Circlehall and truly believe that the timing of this was meant to be because I asked for some advice relating to a role I was applying for and 8 days later I landed the job! I am blown away by the support in this group”</p>
  <p class="quote-author">ROSALIND. HR PROFESSIONAL</p>
  <div class="dots"><span></span><span class="on"></span><span></span><span></span></div>
</section>

<h2 class="team-title">MEET THE TEAM</h2>
<div class="team-rule"></div>
<section class="team">
  <article class="card" style="left:111px;top:2496px;width:310px;height:412px">
    <div class="member-media" role="img" aria-label="Black and white portrait of Maren Holloway"></div>
    <span class="member-badge"></span>
    <h3 class="member-name">MAREN HOLLOWAY</h3>
    <p class="member-role">Founder The Staff Falcons</p>
    <p class="member-bio">Mum and HR Lifer. Lover of the great outdoors and a passion for travel and adventures</p>
  </article>
  <article class="card" style="left:445px;top:2496px;width:310px;height:412px">
    <div class="member-media" role="img" aria-label="Black and white portrait of Dean Ashcroft"></div>
    <span class="member-badge"></span>
    <h3 class="member-name">DEAN ASHCROFT</h3>
    <p class="member-role">Head of Partnerships</p>
    <p class="member-bio">Father of 4, Coach, Golfer and reader of all things 'personal development' "Doubt kills more dreams than failure</p>
  </article>
  <article class="card" style="left:779px;top:2496px;width:310px;height:412px">
    <div class="member-media" role="img" aria-label="Black and white portrait of Tessa Ashcroft"></div>
    <span class="member-badge"></span>
    <h3 class="member-name">TESSA ASHCROFT</h3>
    <p class="member-role">Creative Editor</p>
    <p class="member-bio">Creative, Travel Enthusiast and full-time dog mom "Life is short but the world is wide"</p>
  </article>
</section>

<footer class="site-footer">
  <div class="footer-rule"></div>
  <h2 class="footer-heading">CONTACT</h2>
  <p class="footer-line" style="top:166px">14 - 16 Larkspur Lane London E2 9QT</p>
  <p class="footer-line" style="top:234px">Phone: +1 555 010 2040</p>
  <p class="footer-line" style="top:286px">Email: hq@thestafffalcons.co.uk</p>
  <div class="footer-social"><span></span><span></span><span></span><span></span></div>
  <p class="copyright">©Copyright ©2022 STAFF FALCONS All Rights Reserved.</p>

  <label class="form-label" style="top:96px">Enter Your Name</label>
  <div class="field" style="top:119px;height:52px"></div>
  <label class="form-label" style="top:197px">Enter Your Email*</label>
  <div class="field" style="top:229px;height:53px"></div>
  <label class="form-label" style="top:299px">Enter Your Subject</label>
  <div class="field" style="top:336px;height:53px"></div>
  <label class="form-label" style="top:401px">Message</label>
  <div class="field" style="top:442px;height:107px"></div>
  <span class="btn submit-btn">SUBMIT</span>
</footer>

</body>
</html>
```